Velvet Bloom Marisol's Cleaning Service Business Cards Project

A business card with all contact details with logo design on there (already have a logo) eye catching Logo and contact info on one side, full logo on the back, must target upper class residential and corporate companies, fitness companies, still keep it on the feminine side of things , must look elegant

Target Market(s)

Upper class homes and corporate companies

Industry/Entity Type

Cleaning Service

Contact Information for Business Card

Name: Marisol Denhart
Position: Director
ABN: 47193062857
Email: marisolsvelvetcleaning@brightmail.example
Number: 0418926547

Font styles to use
Decorative

Colors

Designer to choose colors to be used in the design.

Requirements
Must have
• Available Sydney Wide, contact info and logo on one side, full logo on the back
Nice to have
• Professional appearance
Should not have
• Cheap advert looking stuff

```html
<!DOCTYPE html>
<html lang="en">
<head>
<meta charset="utf-8">
<title>Velvet Bloom – Business Card</title>
<link rel="stylesheet" href="https://fonts.googleapis.com/css2?family=Bebas+Neue&family=Lora:wght@500&family=Open+Sans:wght@400&display=swap">
<style>
  :root {
    --canvas-bg: #ebe8e4;
    --card-dark: #2d3341;
    --card-light: #ffffff;
    --teal: #5ec8c8;
    --teal-soft: rgba(94, 200, 200, 0.32);
    --teal-faint: rgba(94, 200, 200, 0.06);
    --tagline: #e6ecee;
    --ink: #1f1f24;
    --rule: #2a2a2a;
  }
  html, body {
    margin: 0;
    padding: 0;
    width: 1200px;
    height: 1000px;
    overflow: hidden;
    background: var(--canvas-bg);
  }
  .canvas {
    position: relative;
    width: 1200px;
    height: 1000px;
  }
  .card {
    position: absolute;
    left: 266px;
    width: 666px;
    height: 396px;
    border-radius: 28px;
    box-shadow: 0 6px 18px rgba(0,0,0,0.18);
  }
  .card--front {
    top: 74px;
    background: var(--card-dark);
  }
  .card--back {
    top: 534px;
    background: var(--card-light);
  }
  .logo-art {
    position: absolute;
    left: 164px;
    top: 64px;
    width: 340px;
    height: 268px;
    border-radius: 16px;
    background: radial-gradient(ellipse at 50% 40%, var(--teal-soft) 0%, var(--teal-faint) 70%, transparent 100%);
  }
  .brand {
    position: absolute;
    left: 0;
    right: 0;
    top: 272px;
    text-align: center;
  }
  .brand__name {
    display: block;
    font-family: "Lora", Georgia, serif;
    font-weight: 500;
    font-size: 38px;
    letter-spacing: 1px;
    line-height: 1;
    color: var(--teal);
  }
  .brand__tagline {
    display: block;
    margin-top: 13px;
    font-family: "Open Sans", Arial, sans-serif;
    font-size: 14px;
    letter-spacing: 3.6px;
    line-height: 1;
    color: var(--tagline);
  }
  .holder {
    position: absolute;
    right: 415px;
    top: 170px;
    text-align: right;
  }
  .holder__name {
    font-family: "Bebas Neue", Impact, sans-serif;
    font-size: 29px;
    line-height: 1;
    color: var(--teal);
    letter-spacing: 0.3px;
  }
  .holder__role {
    margin-top: 4px;
    font-family: "Open Sans", Arial, sans-serif;
    font-size: 16px;
    color: var(--ink);
  }
  .divider {
    position: absolute;
    left: 270px;
    top: 168px;
    width: 1.5px;
    height: 56px;
    background: var(--rule);
  }
  .contacts {
    position: absolute;
    left: 286px;
    top: 164px;
    margin: 0;
    padding: 0;
    list-style: none;
    font-family: "Open Sans", Arial, sans-serif;
    font-size: 15.5px;
    line-height: 22px;
    color: var(--ink);
  }
  .contacts__item {
    display: flex;
    align-items: center;
    gap: 6px;
    white-space: nowrap;
  }
  .contacts__icon {
    width: 15px;
    height: 15px;
    flex: none;
  }
</style>
</head>
<body>
  <main class="canvas">
    <section class="card card--front" aria-label="Card front">
      <div class="logo-art" role="img" aria-label="Brand emblem with ornamental flourishes"></div>
      <div class="brand">
        <span class="brand__name">VELVET BLOOM</span>
        <span class="brand__tagline">MARISOL'S CLEANING SERVICES</span>
      </div>
    </section>

    <section class="card card--back" aria-label="Card back">
      <div class="holder">
        <div class="holder__name">MARISOL DENHART</div>
        <div class="holder__role">Director</div>
      </div>
      <div class="divider"></div>
      <ul class="contacts">
        <li class="contacts__item">ABN: 47193062857</li>
        <li class="contacts__item">
          <svg class="contacts__icon" viewBox="0 0 16 16" aria-hidden="true">
            <path d="M3.5 1.5l2.2 0 1.1 3-1.5 1.2c.8 1.8 2.2 3.2 4 4l1.2-1.5 3 1.1v2.2c0 .8-.7 1.5-1.5 1.5C6.7 13 3 9.3 2 3c0-.8.7-1.5 1.5-1.5z" fill="none" stroke="#5ec8c8" stroke-width="1.2" stroke-linejoin="round"/>
          </svg>
          0418926547
        </li>
        <li class="contacts__item">
          <svg class="contacts__icon" viewBox="0 0 16 16" aria-hidden="true">
            <rect x="1.5" y="3.5" width="13" height="9" fill="none" stroke="#5ec8c8" stroke-width="1.2"/>
            <path d="M1.5 3.5l6.5 5 6.5-5" fill="none" stroke="#5ec8c8" stroke-width="1.2"/>
          </svg>
          marisolsvelvetcleaning@brightmail.example
        </li>
      </ul>
    </section>
  </main>
</body>
</html>
```